Coffee House With Cycling Theme Wants Business Cards

We want to create a business card for a coffee house that has a cycling theme. We expect to use the current logo on one side of the business card and we have been considering adding the words 'COFFEE HOUSE' underneath (see example). For the other side of the business card we want an interesting design with tag-line, address and social media links (the normal business card stuff). See examples provided but we are not fixed on having it exactly as shown, we are very open to great creative ideas. Please note our logo has the initials ‘RM' in orange embedded in the design and this must be retained. However, you can play with the words COFFEE HOUSE as well as use the orange color on the backside of the business card, as you see fit. For an image on the backside of the business card it can be a photo, hand-drawn or whatever but it must visually combine coffee and cycling in some way. The interior of the Coffee House will be reclaimed wood, rustic and have an urban feel to it with cycling artifacts hanging from the walls/ceiling, etc. Finally, it would be beneficial if the business card design elements can be easily used on flyers and other promotional assets. Good luck, we are looking forward to seeing your creative ideas.

Target Market(s)

Coffee lovers and cycling fans

Contact Information for Business Card

See project description.

Colors

Designer to choose colors to be used in the design.

Requirements
Must have
• Must use the current logo provided and combine a coffee and bike theme.
Nice to have
• Orange is used in current logo and could be used as an accent color on the backside of the business card.

```html
<!DOCTYPE html>
<html lang="en">
<head>
<meta charset="utf-8">
<title>RM Coffee House – Business Cards</title>
<link rel="stylesheet" href="https://fonts.googleapis.com/css2?family=Jost:wght@500&display=swap">
<style>
  :root {
    --page: #e9e4df;
    --card-brown: #2e1f1a;
    --orange: #e8642a;
    --cream: #f4ede4;
    --icon-dot: #1f2a4d;
  }
  * { margin: 0; padding: 0; box-sizing: border-box; }
  html, body { width: 1200px; height: 900px; overflow: hidden; }
  body { background: var(--page); position: relative; font-family: "Jost", sans-serif; font-weight: 500; }

  .card {
    position: absolute;
    left: 250px;
    width: 700px;
    height: 400px;
    background: var(--card-brown);
    overflow: hidden;
    box-shadow: 0 6px 18px rgba(0,0,0,0.18);
  }
  .card--front { top: 30px; }
  .card--back { top: 470px; }
  .card-art { position: absolute; inset: 0; width: 700px; height: 400px; }

  .brand-name {
    position: absolute;
    font-family: "Jost", sans-serif;
    font-weight: 500;
    color: var(--orange);
    text-align: center;
    line-height: 1.2;
  }
  .card--front .brand-name { left: 470px; top: 120px; width: 210px; font-size: 36px; }
  .card--back .brand-name { left: 60px; top: 45px; width: 220px; font-size: 28px; }

  .address { position: absolute; left: 110px; top: 168px; color: var(--cream); font-size: 17px; line-height: 36px; }
  .socials { position: absolute; left: 80px; top: 262px; list-style: none; color: var(--cream); font-size: 17px; }
  .socials li { display: flex; align-items: center; height: 44px; }
  .social-dot { width: 26px; height: 26px; border-radius: 50%; background: var(--icon-dot); margin-right: 24px; flex: none; }
</style>
</head>
<body>

<section class="card card--front">
  <svg class="card-art" viewBox="0 0 700 400">
    <defs>
      <linearGradient id="orangeSweep" x1="0" y1="0" x2="0" y2="1">
        <stop offset="0" stop-color="#e8642a"/>
        <stop offset="0.6" stop-color="#b8471c"/>
        <stop offset="1" stop-color="#3a2620"/>
      </linearGradient>
      <radialGradient id="coffeePhoto" cx="0.55" cy="0.4" r="0.7">
        <stop offset="0" stop-color="#4a3022"/>
        <stop offset="0.35" stop-color="#8a8580"/>
        <stop offset="0.7" stop-color="#d9c7b0"/>
        <stop offset="1" stop-color="#6b5040"/>
      </radialGradient>
    </defs>
    <path d="M340,0 H440 C500,120 470,300 345,400 H300 C420,300 430,90 340,0 Z" fill="url(#orangeSweep)"/>
    <path d="M320,0 H345 C440,90 430,300 305,400 H290 C400,300 410,90 320,0 Z" fill="#1e1411"/>
    <path d="M0,0 H320 C410,90 400,300 290,400 H0 Z" fill="url(#coffeePhoto)" role="img" aria-label="Photo of an espresso portafilter filled with ground coffee, beans scattered around"/>
  </svg>
  <p class="brand-name">RM Coffee House</p>
</section>

<section class="card card--back">
  <svg class="card-art" viewBox="0 0 700 400">
    <defs>
      <linearGradient id="slateBand" x1="0" y1="0" x2="1" y2="1">
        <stop offset="0" stop-color="#5b5350"/>
        <stop offset="1" stop-color="#2e1f1a"/>
      </linearGradient>
      <linearGradient id="orangeArc" x1="1" y1="0" x2="0" y2="1">
        <stop offset="0" stop-color="#e8642a"/>
        <stop offset="0.7" stop-color="#c9521f"/>
        <stop offset="1" stop-color="#3a2620"/>
      </linearGradient>
      <radialGradient id="cyclePhoto" cx="0.55" cy="0.4" r="0.7">
        <stop offset="0" stop-color="#7fa6c4"/>
        <stop offset="0.35" stop-color="#c9d6de"/>
        <stop offset="0.55" stop-color="#9a948e"/>
        <stop offset="0.8" stop-color="#d9c7b0"/>
        <stop offset="1" stop-color="#5a3c2a"/>
      </radialGradient>
    </defs>
    <path d="M560,0 H700 C540,30 440,200 410,400 H370 C400,200 470,60 560,0 Z" fill="url(#slateBand)"/>
    <path d="M700,0 C540,30 440,200 410,400 H440 C470,220 560,60 700,24 Z" fill="url(#orangeArc)"/>
    <path d="M700,24 C560,60 470,220 440,400 H452 C482,225 568,70 700,36 Z" fill="#1e1411"/>
    <path d="M700,36 C568,70 482,225 452,400 H700 Z" fill="url(#cyclePhoto)" role="img" aria-label="Photo of a portafilter whose cup shows a sky with clouds and a mountain biker jumping, beans scattered around"/>
  </svg>
  <p class="brand-name">RM Coffee House</p>
  <div class="address">
    <p>Address address</p>
    <p>Map location</p>
  </div>
  <ul class="socials">
    <li><span class="social-dot"></span>rmcoffeehouse</li>
    <li><span class="social-dot"></span>rmcoffeehouse</li>
    <li><span class="social-dot"></span>rmcoffeehouse.com</li>
  </ul>
</section>

</body>
</html>
```